Riverstone & Pine Construction and Developments business cards

A business card with watermark background (construction work)

Company logo attached

Home improvement projects
House renovations
Bathroom and kitchen renovations
House extensions
New builds and granny flats

Director Omar Haddine
(Phone number)
omar@rpcbuildgroup.com.au
(Instagram logo) rpc_buildgroup

```html
<!DOCTYPE html>
<html lang="en">
<head>
<meta charset="utf-8">
<title>Riverstone &amp; Pine Construction and Developments – Business Cards</title>
<link rel="stylesheet" href="https://fonts.googleapis.com/css2?family=Arimo:wght@400;700&display=swap">
<style>
  :root {
    --backdrop: #e9e9e9;
    --card: #fbfbfb;
    --brand-blue: #2a6db3;
    --ink: #3a3a3a;
    --rule: #333333;
  }
  * { box-sizing: border-box; margin: 0; padding: 0; }
  html, body { width: 1200px; height: 801px; overflow: hidden; }
  body {
    background: var(--backdrop);
    font-family: "Arimo", Arial, sans-serif;
    color: var(--ink);
    position: relative;
  }
  .card {
    position: absolute;
    top: 246px;
    width: 540px;
    height: 309px;
    background: var(--card);
    box-shadow: 0 6px 18px rgba(0,0,0,0.18);
  }
  .card--contact { left: 40px; }
  .card--services { left: 620px; }

  .brand {
    display: flex;
    align-items: center;
    gap: 10px;
  }
  .brand__mark {
    width: 22px;
    height: 22px;
    background: var(--brand-blue);
    flex: none;
  }
  .brand__name {
    color: var(--brand-blue);
    font-weight: 700;
    line-height: 1.2;
  }

  /* contact side */
  .card--contact .brand {
    position: absolute;
    left: 34px;
    top: 112px;
    width: 200px;
  }
  .card--contact .brand__name { font-size: 17px; }
  .divider {
    position: absolute;
    left: 252px;
    top: 74px;
    width: 1px;
    height: 160px;
    background: var(--rule);
  }
  .person {
    position: absolute;
    left: 274px;
    top: 82px;
  }
  .person__name {
    color: var(--brand-blue);
    font-size: 22px;
    font-weight: 700;
  }
  .person__role {
    font-size: 15px;
    margin-top: 2px;
  }
  .contact-list {
    list-style: none;
    margin-top: 22px;
    font-size: 14px;
  }
  .contact-list li {
    display: flex;
    align-items: center;
    gap: 8px;
    margin-bottom: 7px;
  }
  .contact-list svg { width: 15px; height: 15px; flex: none; }
  .social-square {
    width: 13px; height: 13px;
    background: var(--brand-blue);
    border-radius: 3px;
    flex: none;
    margin: 0 1px;
  }

  /* services side */
  .card--services .brand {
    position: absolute;
    left: 0; right: 0;
    top: 62px;
    justify-content: center;
  }
  .card--services .brand__name { font-size: 22px; text-align: left; }
  .card--services .brand__mark { width: 28px; height: 28px; }
  .services {
    position: absolute;
    left: 0; right: 0;
    top: 178px;
    text-align: center;
    font-size: 15px;
    line-height: 1.55;
  }
  .services span::before {
    content: "•";
    color: var(--brand-blue);
    margin: 0 6px 0 10px;
  }
</style>
</head>
<body>
  <section class="card card--contact">
    <div class="brand">
      <span class="brand__mark"></span>
      <span class="brand__name">Riverstone &amp; Pine Construction and Developments</span>
    </div>
    <div class="divider"></div>
    <div class="person">
      <p class="person__name">Omar Haddine</p>
      <p class="person__role">Director</p>
      <ul class="contact-list">
        <li>
          <svg viewBox="0 0 24 24" aria-hidden="true"><path fill="#2a6db3" d="M6.6 10.8a15 15 0 0 0 6.6 6.6l2.2-2.2c.3-.3.7-.4 1-.2 1.1.4 2.3.6 3.6.6.6 0 1 .4 1 1V20c0 .6-.4 1-1 1A17 17 0 0 1 3 4c0-.6.4-1 1-1h3.5c.6 0 1 .4 1 1 0 1.3.2 2.5.6 3.6.1.3 0 .7-.2 1z"/></svg>
          123-555-0148
        </li>
        <li>
          <svg viewBox="0 0 24 24" aria-hidden="true"><rect x="2" y="5" width="20" height="14" fill="#2a6db3"/><path d="M2 5l10 8 10-8" fill="none" stroke="#fbfbfb" stroke-width="1.8"/></svg>
          omar@rpcbuildgroup.com.au
        </li>
        <li>
          <span class="social-square"></span>
          rpc_buildgroup
        </li>
      </ul>
    </div>
  </section>

  <section class="card card--services">
    <div class="brand">
      <span class="brand__mark"></span>
      <span class="brand__name">Riverstone &amp; Pine<br>Construction and Developments</span>
    </div>
    <p class="services">
      <span>Home improvement projects</span><span>House renovations</span><br>
      <span>Bathroom and kitchen renovations</span><span>House extensions</span><br>
      <span>New builds and granny flats</span>
    </p>
  </section>
</body>
</html>
```